Tarvimoor business cards

Need fresh design for our business cards. Logo must be specific, we are open for everything else.

Contact Information for Business Card

phrase "GMP & JANITORIAL SERVICES" should be used as main point of card

Colors
3176b5
3276b5
85acd3
cedeed
ffffff
0292cd
33a6d7
85cae6
cee9f5

Requirements
Must have
• The logo
Should not have
• crowded designs

```html
<!DOCTYPE html>
<html lang="en">
<head>
<meta charset="utf-8">
<title>Tarvimoor business cards</title>
<link href="https://fonts.googleapis.com/css2?family=Josefin+Sans:wght@400&family=Lato:wght@300;400;700&display=swap" rel="stylesheet">
<style>
  :root{
    --blue-deep:#1590cf;
    --blue-mid:#2ea3d8;
    --blue-light:#19b8e0;
    --blue-text:#1f9ad6;
    --white:#ffffff;
    --canvas:#d9d9d9;
  }
  *{margin:0;padding:0;box-sizing:border-box}
  html,body{width:1200px;height:1200px;overflow:hidden;background:var(--canvas)}
  .sheet{position:relative;width:1200px;height:1200px}
  .card{position:absolute;top:250px;width:400px;height:700px;overflow:hidden;box-shadow:0 6px 20px rgba(0,0,0,.18)}
  .card-front{left:150px;background:var(--white)}
  .card-back{left:650px;background:linear-gradient(160deg,var(--blue-light) 0%,var(--blue-mid) 45%,var(--blue-deep) 100%)}
  .shapes{position:absolute;inset:0}
  .wordmark{font-family:"Josefin Sans",sans-serif;font-weight:400;letter-spacing:6px;white-space:nowrap;display:flex;align-items:center;gap:10px}
  .wordmark .dot{width:10px;height:10px;border-radius:50%}
  .front-logo{position:absolute;top:235px;left:0;right:0;justify-content:center;font-size:38px;color:var(--blue-text)}
  .front-logo .dot{background:var(--blue-text)}
  .front-tagline{position:absolute;top:295px;left:0;right:0;text-align:center;font-family:Lato,sans-serif;font-weight:300;font-size:17px;letter-spacing:.5px;color:var(--blue-text)}
  .contact{position:absolute;left:95px;top:440px;color:var(--white);font-family:Lato,sans-serif}
  .person-name{font-weight:700;font-size:17px;letter-spacing:.5px}
  .person-role{font-weight:300;font-size:15px;margin-top:2px}
  .person-phone{font-weight:700;font-size:16px;margin-top:2px;display:flex;align-items:center;gap:5px}
  .details{list-style:none;margin-top:34px;font-size:14px;font-weight:400;line-height:1.5}
  .details li{display:flex;align-items:center;gap:8px}
  .details .indent{padding-left:22px}
  .icon{width:14px;height:14px;flex:none}
  .back-logo{position:absolute;top:260px;left:0;right:0;justify-content:center;font-size:38px;color:var(--white)}
  .back-logo .dot{background:var(--white)}
  .back-url{position:absolute;top:312px;left:0;right:0;text-align:center;font-family:Lato,sans-serif;font-size:11px;color:var(--white)}
  .back-tagline{position:absolute;top:375px;left:0;right:0;text-align:center;font-family:Lato,sans-serif;font-weight:300;font-size:17px;letter-spacing:.5px;color:var(--white)}
</style>
</head>
<body>
<main class="sheet">
  <section class="card card-front">
    <svg class="shapes" width="400" height="700" viewBox="0 0 400 700">
      <polygon points="150,0 380,0 380,150 205,150" fill="var(--blue-mid)" stroke="var(--blue-mid)" stroke-width="14" stroke-linejoin="round"/>
      <polygon points="70,700 70,470 200,360 400,360 400,700" fill="var(--blue-mid)" stroke="var(--blue-mid)" stroke-width="14" stroke-linejoin="round"/>
    </svg>
    <div class="wordmark front-logo"><span class="dot"></span>TARVIMOOR</div>
    <p class="front-tagline">GMP &amp; JANITORIAL SERVICES</p>
    <div class="contact">
      <p class="person-name">ABC XXXXX</p>
      <p class="person-role">Managing Director</p>
      <p class="person-phone">
        <svg class="icon" viewBox="0 0 16 16"><circle cx="8" cy="8" r="8" fill="#fff"/><path d="M5 4.5l1.5-.5 1 2-1 .8a5 5 0 002.7 2.7l.8-1 2 1-.5 1.5c-3.5.2-6.7-3-6.5-6.5z" fill="var(--blue-mid)"/></svg>
        555 018 3371
      </p>
      <ul class="details">
        <li><svg class="icon" viewBox="0 0 16 16"><circle cx="8" cy="8" r="8" fill="#fff"/><path d="M5 4.5l1.5-.5 1 2-1 .8a5 5 0 002.7 2.7l.8-1 2 1-.5 1.5c-3.5.2-6.7-3-6.5-6.5z" fill="var(--blue-mid)"/></svg>(555) 014-2290</li>
        <li><svg class="icon" viewBox="0 0 16 16"><circle cx="8" cy="8" r="8" fill="#fff"/><rect x="4" y="5" width="8" height="6" fill="var(--blue-mid)"/><path d="M4 5l4 3 4-3" stroke="#fff" fill="none"/></svg>info@tarvimoor.com</li>
        <li><svg class="icon" viewBox="0 0 16 16"><circle cx="8" cy="8" r="8" fill="#fff"/><path d="M8 3.5a3 3 0 013 3c0 2.2-3 5.5-3 5.5S5 8.7 5 6.5a3 3 0 013-3z" fill="var(--blue-mid)"/><circle cx="8" cy="6.5" r="1" fill="#fff"/></svg>50 Ashby Road</li>
        <li class="indent">Hollinvale HC 06180</li>
        <li><svg class="icon" viewBox="0 0 16 16"><circle cx="8" cy="8" r="8" fill="#fff"/><circle cx="8" cy="8" r="3.5" fill="none" stroke="var(--blue-mid)" stroke-width="1.4"/></svg>www.tarvimoor.com</li>
      </ul>
    </div>
  </section>

  <section class="card card-back">
    <div class="wordmark back-logo"><span class="dot"></span>TARVIMOOR</div>
    <p class="back-url">www.tarvimoor.com</p>
    <p class="back-tagline">GMP &amp; JANITORIAL SERVICES</p>
  </section>
</main>
</body>
</html>
```